Web site design for news feed - Talvenor Live

We need to design a webpage to promote our web scraping newsfeed (similar to pagewheel) the name of the business is "Talvenor Live" ( a subsidiary of our company Talvenor - see www.corvel-holdings.example for details, DO NOT BASE THAT WEBSITE ON YOUR DESIGN).

We are inspired by famous Economists, we are inspired by empirical data, accuracy, but importantly the site needs to portray our "new approach" to delivering functional and "boring" financial news flow (pagewheel)

Websites we like:

www.zolvo.example - love the graphics
www.pagewheel.example - love the functionality
http://www.marketdial.example/ - practical
http://www.wirepost.example/ - practical
http://www.quenbrix.example/en-us/default.aspx
www.ldg.example
http://www.harbortimes.example/
www.velto.example

Our logo is attached

We like black and white, artful, mabel tunn etc
Updates

Hi All, please bear in mind that this is a NEWS site (it will need space to post stories) - so whilst the visual aspect is really important, the functionally around the amount of stories we can post is important too.

think marketdial.example, www.pitcrest.example, www.ldg.example - but feel (creativity) is zolvo.example, pagewheel.example

thanks all for some great designs.

i will revert to those closest tomorrow.
in the meantime, please bear in mind that the vision of skylines and economists helps me get to the design immediately, it resonates better, it helps me visually decide. 
lastly, in terms of the news "spaces", i will need to have 6 "top stories" and then room for maybe 20 more headlines..the top stories will need a picture, the 20 others will not (just headline text).
Thanks everyone again

Industry/Entity Type

Financial

Font styles to use
Serif
Sans Serif

```html
<!DOCTYPE html>
<html lang="en">
<head>
<meta charset="utf-8">
<title>Talvenor Live</title>
<link href="https://fonts.googleapis.com/css2?family=Open+Sans:wght@400;600;700&family=PT+Serif:ital,wght@0,400;0,700;1,400&family=Roboto+Condensed:wght@400;700&display=swap" rel="stylesheet">
<style>
:root{
  --ink:#1a1a1a;
  --black:#111;
  --bar:#222;
  --red:#c8102e;
  --navy:#1d2f4c;
  --grey:#8a8a8a;
  --rule:#d6d6d6;
  --paper:#f2f2f2;
  --white:#fff;
  --sky-a:#6d6d6d;
  --sky-b:#d9d9d9;
}
*{box-sizing:border-box;margin:0;padding:0}
html,body{width:1200px;height:2280px;overflow:hidden}
body{font-family:"Open Sans",Arial,sans-serif;color:var(--ink);background:var(--white)}
.wrap{width:1120px;margin:0 auto;position:relative}

/* utility bar */
.util{height:44px;background:var(--bar);color:#ccc;font-size:12px}
.util .wrap{display:flex;align-items:center;height:44px;gap:18px}
.util .trend{color:var(--red);font-family:"Roboto Condensed",sans-serif;font-weight:700;letter-spacing:.5px}
.util .links span{margin-right:14px}
.util .right{margin-left:auto;display:flex;gap:8px;align-items:center}
.sq{width:16px;height:16px;background:#777;display:inline-block}
.util .right .acct{margin-left:10px;color:#ddd}

/* masthead */
.mast{height:116px}
.mast .wrap{display:flex;align-items:center;height:116px}
.brand{display:flex;align-items:center;gap:14px}
.brand .mark{width:34px;height:34px;background:var(--black);flex:none}
.brand .name{font-family:"Open Sans",sans-serif;font-weight:600;font-size:30px;line-height:1.05;color:var(--black)}
.ad-top{margin-left:auto;width:728px;height:90px;border:1px solid var(--rule);display:flex;align-items:center;background:#fafafa}
.ad-top .txt{font-family:"Roboto Condensed",sans-serif;font-size:34px;padding-left:40px;color:var(--ink);white-space:nowrap}
.ad-top .txt b{font-weight:700}
.ad-top .img{margin-left:auto;width:220px;height:88px;background:linear-gradient(135deg,#2b2b2b,#9a9a9a)}

/* nav */
.nav{height:40px;background:var(--black)}
.nav ul{list-style:none;display:flex;height:40px;align-items:center}
.nav li{font-family:"Roboto Condensed",sans-serif;font-weight:700;color:var(--white);font-size:17px;padding:0 22px;border-right:1px solid #333;line-height:40px;white-space:nowrap}
.nav li:first-child{padding-left:14px}
.nav li.on{background:#333}

/* hero */
.hero{height:440px;position:relative}
.hero .photo{position:absolute;inset:0;background:linear-gradient(180deg,var(--sky-b) 0%,#a5a5a5 40%,var(--sky-a) 100%)}
.hero .label{position:absolute;left:80px;top:34px;background:var(--black);color:var(--white);font-family:"Roboto Condensed",sans-serif;font-size:26px;padding:4px 14px}
.hero .label b{font-weight:700}
.hero .lead{position:absolute;left:80px;top:84px;width:300px;background:rgba(255,255,255,.9);padding:16px 18px}
.hero .lead h1{font-family:"PT Serif",serif;font-size:24px;line-height:1.2;color:var(--red);margin-bottom:10px}
.hero .lead p{font-size:12px;line-height:1.5;color:#444}
.hero .lead a{color:var(--red);font-weight:700;text-decoration:none}
.tabs{position:absolute;left:40px;right:40px;bottom:14px;display:flex;gap:6px}
.tab{flex:1;height:92px;background:rgba(20,20,20,.85);padding:10px 12px}
.tab h3{font-family:"Roboto Condensed",sans-serif;color:var(--red);font-size:13px;margin-bottom:6px}
.tab p{color:#ddd;font-size:11px;line-height:1.4}

/* subscribe */
.sub{height:72px;border-bottom:1px solid var(--rule)}
.sub .wrap{display:flex;align-items:center;height:72px}
.sub h2,.sub .follow{font-family:"Roboto Condensed",sans-serif;font-size:24px;color:var(--ink);font-weight:700}
.sub .field{margin-left:20px;width:420px;height:34px;border:1px solid var(--rule);font-size:12px;color:var(--grey);padding:8px 10px}
.sub .go{width:44px;height:34px;background:var(--red);color:#fff;font-weight:700;font-size:13px;text-align:center;line-height:34px}
.sub .follow{margin-left:auto;display:flex;align-items:center;gap:10px}
.sub .follow .sq{width:24px;height:24px;background:#444}

/* main */
.main{height:1408px;background:var(--paper);padding-top:24px}
.main .wrap{display:flex;gap:40px}
.heads{width:740px}
.sec-title{font-family:"Roboto Condensed",sans-serif;font-size:26px;color:var(--red);font-weight:400;border-bottom:2px solid var(--rule);padding-bottom:8px;margin-bottom:14px}
.grid{display:grid;grid-template-columns:1fr 1fr;column-gap:40px}
.story{height:112px;border-bottom:1px solid var(--rule);padding-top:16px}
.story h4{font-family:"PT Serif",serif;font-size:19px;line-height:1.25;color:var(--navy);font-weight:700}
.story time{display:block;font-size:11px;color:var(--grey);margin-top:6px}
.ad-mid{height:130px;margin:22px 0;display:flex;align-items:center;background:#fbfaf6;border:1px solid var(--rule)}
.ad-mid .copy{padding-left:30px;white-space:nowrap}
.ad-mid .copy small{display:block;font-style:italic;font-family:"PT Serif",serif;font-size:14px;color:#777;margin-bottom:4px}
.ad-mid .copy strong{font-family:"Roboto Condensed",sans-serif;font-size:28px;color:#555;letter-spacing:1px}
.ad-mid .img{margin-left:36px;width:170px;height:70px;background:linear-gradient(90deg,#3a3a3a,#8a8a8a);flex:none}
.ad-mid .brand-name{margin-left:auto;margin-right:30px;font-weight:700;font-size:22px;color:var(--ink)}
.popular{width:340px}
.pop{margin-bottom:36px}
.pop .img{width:100%;height:190px}
.pop h4{font-family:"PT Serif",serif;font-size:18px;line-height:1.25;color:var(--navy);margin-top:10px}
.pop p{font-size:11px;color:#666;line-height:1.5;margin-top:4px}
.pop time{font-size:11px;color:var(--grey)}

/* footer */
.foot{height:160px;background:var(--bar);color:#bbb;font-size:11px}
.foot .wrap{display:flex;padding-top:26px;height:118px}
.foot .brand .mark{background:#fff;width:26px;height:26px}
.foot .brand .name{color:#fff;font-size:20px}
.foot .social{display:flex;gap:6px;margin-top:14px}
.foot .social .sq{background:#666;width:16px;height:16px}
.foot .col{margin-left:70px;line-height:1.6}
.foot .col:first-of-type{margin-left:110px}
.foot .col h5{color:#fff;font-size:11px;font-weight:700;margin-bottom:4px}
.foot .bottom{border-top:1px solid #3a3a3a}
.foot .bottom .wrap{height:42px;padding:0;align-items:center;display:flex}
.foot .bottom .links{margin-left:auto;display:flex;gap:24px}
</style>
</head>
<body>

<div class="util">
  <div class="wrap">
    <span class="trend">TRENDING NOW</span>
    <span class="links"><span>Rates hold steady</span><span>Oil dips lower</span><span>Bond yields climb</span><span>Earnings week</span></span>
    <span class="right"><i class="sq"></i><i class="sq"></i><i class="sq"></i><span class="acct">REGISTER &nbsp; SIGN IN</span></span>
  </div>
</div>

<header class="mast">
  <div class="wrap">
    <div class="brand"><span class="mark"></span><span class="name">Talvenor<br>Live</span></div>
    <div class="ad-top">
      <span class="txt">IT'S HERE <b>Pixora 5</b></span>
      <div class="img" role="img" aria-label="Advertisement product photo of a phone"></div>
    </div>
  </div>
</header>

<nav class="nav">
  <div class="wrap">
    <ul>
      <li class="on">HOME</li><li>NEWS</li><li>QUICK</li><li>OPINION</li><li>MARKETS</li><li>PERSONAL FINANCE</li><li>TECH</li><li>POLITICS</li><li>VIDEO</li>
    </ul>
  </div>
</nav>

<section class="hero">
  <div class="photo" role="img" aria-label="Black and white aerial photograph of a city skyline"></div>
  <div class="label">top <b>STORIES</b></div>
  <article class="lead">
    <h1>Lorem ipsum dolor sit amet, consectetur</h1>
    <p>adipiscing elit, sed do eiusmod tempor incididunt ut labore et dolore magna aliqua. Ut enim ad minim veniam. <a>Read more</a></p>
  </article>
  <div class="tabs">
    <div class="tab"><h3>STOCKS</h3><p>Even the high-cap stocks saw a quiet session</p></div>
    <div class="tab"><h3>NEWS</h3><p>Lorem ipsum dolor sit amet consectetur adipiscing elit</p></div>
    <div class="tab"><h3>POLITICS</h3><p>Lorem ipsum dolor sit amet consectetur adipiscing elit</p></div>
    <div class="tab"><h3>TRADES</h3><p>Lorem ipsum dolor sit amet consectetur adipiscing elit</p></div>
    <div class="tab"><h3>MARKETS</h3><p>Lorem ipsum dolor sit amet consectetur adipiscing elit</p></div>
    <div class="tab"><h3>OPINION</h3><p>Lorem ipsum dolor sit amet consectetur adipiscing elit</p></div>
  </div>
</section>

<section class="sub">
  <div class="wrap">
    <h2>SUBSCRIBE</h2>
    <div class="field">Enter your email address</div>
    <div class="go">GO</div>
    <div class="follow">FOLLOW US <i class="sq"></i><i class="sq"></i><i class="sq"></i><i class="sq"></i></div>
  </div>
</section>

<main class="main">
  <div class="wrap">
    <section class="heads">
      <h2 class="sec-title">Headline</h2>
      <div class="grid">
        <div class="story"><h4>Phasellus tempus quam ut quam tempor pretium quisque.</h4><time>2 hours ago</time></div>
        <div class="story"><h4>Maecenas vel orci a lorem tincidunt tempus nec.</h4><time>2 hours ago</time></div>
        <div class="story"><h4>Etiam porttitor accumsan pellentesque sapien felis.</h4><time>2 hours ago</time></div>
        <div class="story"><h4>Praesent non massa sit amet purus volutpat et eleifend est.</h4><time>2 hours ago</time></div>
        <div class="story"><h4>Vestibulum ut justo ut urna hendrerit gravida eu ac eros.</h4><time>2 hours ago</time></div>
        <div class="story"><h4>Phasellus tempus quam ut quam tempor pretium quisque.</h4><time>2 hours ago</time></div>
        <div class="story"><h4>Phasellus tempus quam ut quam tempor pretium quisque.</h4><time>2 hours ago</time></div>
        <div class="story"><h4>Sed iaculis hendrerit mauris vitae dignissim.</h4><time>2 hours ago</time></div>
        <div class="story"><h4>Donec vitae neque at quam rhoncus hendrerit.</h4><time>2 hours ago</time></div>
        <div class="story"><h4>Phasellus tempus quam ut quam tempor pretium quisque.</h4><time>2 hours ago</time></div>
      </div>
      <div class="ad-mid">
        <div class="copy"><small>Super slim wallets designed to...</small><strong>SET YOUR POCKETS FREE</strong></div>
        <div class="img" role="img" aria-label="Advertisement photo of slim leather wallets"></div>
        <span class="brand-name">Pocketa</span>
      </div>
      <div class="grid">
        <div class="story"><h4>Phasellus tempus quam ut quam tempor pretium quisque.</h4><time>2 hours ago</time></div>
        <div class="story"><h4>Maecenas vel orci a lorem tincidunt tempus nec.</h4><time>2 hours ago</time></div>
        <div class="story"><h4>Etiam porttitor accumsan pellentesque sapien felis.</h4><time>2 hours ago</time></div>
        <div class="story"><h4>Praesent non massa sit amet purus volutpat et eleifend est.</h4><time>2 hours ago</time></div>
        <div class="story"><h4>Vestibulum ut justo ut urna hendrerit gravida eu ac eros.</h4><time>2 hours ago</time></div>
        <div class="story"><h4>Phasellus tempus quam ut quam tempor pretium quisque.</h4><time>2 hours ago</time></div>
        <div class="story"><h4>Phasellus tempus quam ut quam tempor pretium quisque.</h4><time>2 hours ago</time></div>
        <div class="story"><h4>Sed iaculis hendrerit mauris vitae dignissim.</h4><time>2 hours ago</time></div>
        <div class="story"><h4>Donec vitae neque at quam rhoncus hendrerit.</h4><time>2 hours ago</time></div>
        <div class="story"><h4>Phasellus tempus quam ut quam tempor pretium quisque.</h4><time>2 hours ago</time></div>
      </div>
    </section>

    <aside class="popular">
      <h2 class="sec-title">Popular</h2>
      <article class="pop">
        <div class="img" role="img" aria-label="News photo of a person speaking" style="background:linear-gradient(135deg,#4a4a4a,#a58a6e)"></div>
        <h4>Phasellus tempus quam ut quam tempor pretium</h4>
        <p>Lorem ipsum dolor sit amet, consectetur adipiscing elit sed do.</p>
        <time>2 hours ago</time>
      </article>
      <article class="pop">
        <div class="img" role="img" aria-label="News photo of a laptop on a desk" style="background:linear-gradient(135deg,#8aa0c0,#e6e6e6)"></div>
        <h4>Phasellus tempus quam ut quam tempor pretium</h4>
        <p>Lorem ipsum dolor sit amet, consectetur adipiscing elit sed do.</p>
        <time>2 hours ago</time>
      </article>
      <article class="pop">
        <div class="img" role="img" aria-label="Photo of handwritten equations on a chalkboard" style="background:linear-gradient(135deg,#0d1a33,#3b5680)"></div>
        <h4>Phasellus tempus quam ut quam tempor pretium</h4>
        <p>Lorem ipsum dolor sit amet, consectetur adipiscing elit sed do.</p>
        <time>2 hours ago</time>
      </article>
      <article class="pop">
        <div class="img" role="img" aria-label="Black and white portrait photo" style="background:linear-gradient(135deg,#1e1e1e,#8c8c8c)"></div>
        <h4>Phasellus tempus quam ut quam tempor pretium</h4>
        <p>Lorem ipsum dolor sit amet, consectetur adipiscing elit sed do.</p>
        <time>2 hours ago</time>
      </article>
    </aside>
  </div>
</main>

<footer class="foot">
  <div class="wrap">
    <div>
      <div class="brand"><span class="mark"></span><span class="name">Talvenor<br>Live</span></div>
      <div class="social"><i class="sq"></i><i class="sq"></i><i class="sq"></i><i class="sq"></i><i class="sq"></i></div>
    </div>
    <div class="col"><h5>ABOUT TALVENOR</h5>Our Company<br>Careers<br>Advertising<br>Press Room</div>
    <div class="col"><h5>SUPPORT &amp; CONTACT</h5>Customer Support<br>Feedback<br>Help<br>Sitemap</div>
    <div class="col"><h5>TALVENOR LIVE NETWORK</h5>Talvenor Business<br>Talvenor Markets<br>Talvenor Trading<br>Talvenor Research</div>
    <div class="col"><h5>OTHERS</h5>Newsletters<br>Subscriber Login<br>RSS</div>
  </div>
  <div class="bottom">
    <div class="wrap">
      <span>&copy;2013 Talvenor Live. All Rights Reserved</span>
      <span class="links"><span>Trademarks</span><span>Terms of Service</span><span>Privacy Policy</span><span>Ad Choices</span></span>
    </div>
  </div>
</footer>

</body>
</html>
```